Veltrium stationery design

Design stationery for us that fits with the colours of the logo. We are looking for letterheads, business cards etc. Something we can use for a prospectus and marketing presentations in power point. Must be completed in such a manner that it represents a corporate image for large enterprise clients and other large organisations. The company is a project assurance and monitoring company that works in all industries.

```html
<!DOCTYPE html>
<html lang="en">
<head>
<meta charset="utf-8">
<title>Veltrium stationery</title>
<link href="https://fonts.googleapis.com/css2?family=Poppins:wght@400;600;700&display=swap" rel="stylesheet">
<style>
  :root {
    --navy: #163a7a;
    --blue: #1d4f9c;
    --purple: #5a3f6e;
    --orange: #ee6a1f;
    --red: #e3202a;
    --ink: #1d2c55;
    --paper: #ffffff;
    --scene: #e6e6e6;
    --page-bg: #ffffff;
    --brand-stripe: linear-gradient(90deg, var(--blue) 0%, var(--navy) 30%, var(--purple) 55%, var(--orange) 78%, var(--red) 100%);
  }
  * { margin: 0; padding: 0; box-sizing: border-box; }
  html, body { width: 782px; height: 1200px; overflow: hidden; background: var(--page-bg); }
  body { position: relative; font-family: "Poppins", sans-serif; color: var(--ink); }

  .cards-area { position: absolute; left: 0; top: 0; width: 782px; height: 650px; background: var(--scene); }
  .card {
    position: absolute; width: 330px; height: 190px; background: var(--paper);
    box-shadow: 0 8px 18px rgba(0,0,0,.18); overflow: hidden;
  }
  .card--front { left: 36px; top: 150px; }
  .card--back { left: 414px; top: 310px; }
  .card .stripe { position: absolute; left: 0; right: 0; bottom: 0; height: 6px; background: var(--brand-stripe); }

  .wordmark { font-weight: 700; color: var(--blue); letter-spacing: .02em; display: flex; align-items: center; }
  .wordmark .dot { display: inline-block; border-radius: 50%; background: var(--red); margin-right: .4em; }

  .card--front .wordmark { position: absolute; left: 22px; top: 22px; font-size: 15px; }
  .card--front .wordmark .dot { width: 14px; height: 14px; }
  .card--front .contact { position: absolute; left: 22px; bottom: 30px; font-size: 9px; }
  .card--front .person { position: absolute; right: 22px; top: 80px; text-align: right; }
  .person .name { font-weight: 700; font-size: 16px; color: var(--blue); line-height: 1.1; }
  .person .role { font-size: 9px; color: var(--ink); }

  .card--back .wordmark { position: absolute; left: 0; right: 0; top: 0; bottom: 6px; justify-content: center; font-size: 28px; }
  .card--back .wordmark .dot { width: 24px; height: 24px; }

  .contact li { list-style: none; display: flex; align-items: center; gap: 5px; line-height: 1.55; }
  .contact svg { width: 8px; height: 8px; fill: var(--blue); flex: none; }

  .sheet { position: absolute; top: 673px; width: 343px; height: 443px; background: var(--paper); box-shadow: 0 4px 16px rgba(0,0,0,.22); overflow: hidden; }
  .sheet .stripe { position: absolute; left: 0; right: 0; bottom: 0; height: 8px; background: var(--brand-stripe); }

  .letterhead { left: 36px; }
  .letterhead .wordmark { position: absolute; left: 27px; top: 30px; font-size: 14px; }
  .letterhead .wordmark .dot { width: 14px; height: 14px; }
  .letterhead .contact { position: absolute; left: 245px; top: 27px; font-size: 6px; }
  .letterhead .contact li { line-height: 1.5; gap: 4px; }
  .letterhead .contact svg { width: 5px; height: 5px; }

  .cover { left: 396px; }
  .cover .hero {
    position: absolute; left: 0; top: 0; width: 100%; height: 262px;
    background: linear-gradient(160deg, #1a5aa8 0%, #17468f 40%, #1e3e80 65%, #4e3f70 100%);
  }
  .cover .title { position: absolute; left: 37px; top: 160px; color: #fff; font-weight: 700; font-size: 40px; line-height: 1; letter-spacing: .01em; }
  .cover .subtitle { position: absolute; left: 37px; top: 207px; color: #fff; font-weight: 700; font-size: 18px; line-height: 1.25; }
  .cover .wordmark { position: absolute; left: 0; right: 0; top: 330px; justify-content: center; font-size: 24px; }
  .cover .wordmark .dot { width: 22px; height: 22px; }
</style>
</head>
<body>

<section class="cards-area">
  <article class="card card--front">
    <div class="wordmark"><span class="dot"></span>VELTRIUM</div>
    <div class="person">
      <div class="name">Person Name</div>
      <div class="role">Designation</div>
    </div>
    <ul class="contact">
      <li><svg viewBox="0 0 10 10"><path d="M2 0.5 3.8 2.6 2.9 3.7Q4 6 6.3 7.1L7.4 6.2 9.5 8 8.3 9.5Q1.5 8.5 0.5 1.7Z"/></svg>555-014-2086</li>
      <li><svg viewBox="0 0 10 10"><path d="M0 2h10v6H0z M0 2l5 3.5L10 2" /></svg>hello@veltrium.com</li>
      <li><svg viewBox="0 0 10 10"><circle cx="5" cy="5" r="4.5"/></svg>www.veltrium.com</li>
    </ul>
    <div class="stripe"></div>
  </article>

  <article class="card card--back">
    <div class="wordmark"><span class="dot"></span>VELTRIUM</div>
    <div class="stripe"></div>
  </article>
</section>

<article class="sheet letterhead">
  <div class="wordmark"><span class="dot"></span>VELTRIUM</div>
  <ul class="contact">
    <li><svg viewBox="0 0 10 10"><path d="M2 0.5 3.8 2.6 2.9 3.7Q4 6 6.3 7.1L7.4 6.2 9.5 8 8.3 9.5Q1.5 8.5 0.5 1.7Z"/></svg>555-014-2086</li>
    <li><svg viewBox="0 0 10 10"><path d="M0 2h10v6H0z"/></svg>hello@veltrium.com</li>
    <li><svg viewBox="0 0 10 10"><circle cx="5" cy="5" r="4.5"/></svg>www.veltrium.com</li>
  </ul>
  <div class="stripe"></div>
</article>

<article class="sheet cover">
  <div class="hero" role="img" aria-label="Deep blue to purple brand backdrop"></div>
  <h1 class="title">VELTRIUM</h1>
  <p class="subtitle">PROJECT ASSURANCE &amp;<br>MONITORING COMPANY</p>
  <div class="wordmark"><span class="dot"></span>VELTRIUM</div>
  <div class="stripe"></div>
</article>

</body>
</html>
```